Redesign of existing template to align with brand identify

We need page template redesign for our teach English abroad content cluster. Our dev guy created a mockup for a page template, although decent, it needs a designer's touch to elevate it and make sure it aligns with our existing brand identity on the website. The mockup has been created on figma and we would prefer the design files to include figma files.

The designer can either work from scratch or they work on the design we already have on the figma link - https://www.plankboard.io/file/Q7rTm2Xp9KdLwa4VbNcYhZ/Page-Layout-Draft?node-id=48%3A15&t=xk4PqLmZr8sWvT2a-7

We need a design for both desktop and mobile layout. You can visit our website here https://www.bramblequillinstitute.com/ to see our brand colors and style. We want to use a lot of white space on the design with a hint of our brand colors.

Video 1 - https://clipharbor.net/472615830/3d1fa7c9e4 >> watch this one first
Video 2 - https://clipharbor.net/472618264/e6c2b5a7d1

```html
<!DOCTYPE html>
<html lang="en">
<head>
<meta charset="utf-8">
<title>Teach English in South Korea</title>
<link href="https://fonts.googleapis.com/css2?family=Josefin+Sans:wght@600;700&family=Barlow:wght@400;500;600&family=Roboto:wght@400;500&display=swap" rel="stylesheet">
<style>
:root{
  --teal:#1dc2c7;
  --navy:#0f2c4c;
  --ink:#222;
  --body:#666;
  --muted:#888;
  --pill:#e9e9e9;
  --dark:#2b2b2b;
  --grey-bg:#f4f4f4;
}
*{box-sizing:border-box;margin:0;padding:0}
html,body{width:1200px;height:4052px;overflow:hidden}
body{position:relative;background:#fff;font-family:"Barlow",sans-serif;color:var(--body)}
.abs{position:absolute}
.head-font{font-family:"Josefin Sans",sans-serif;font-weight:700;color:var(--navy)}

/* header */
.site-header{left:0;top:0;width:1200px;height:78px;background:#fff}
.brand{left:120px;top:16px;display:flex;align-items:center;gap:8px}
.brand-mark{width:14px;height:14px;background:var(--teal);border-radius:50%}
.brand-name{font-family:"Barlow",sans-serif;font-weight:600;font-size:15px;color:var(--navy)}
.search{left:898px;top:15px;width:124px;height:20px;border:1px solid #999;font-size:7px;padding:5px 4px;color:#999;display:flex;justify-content:space-between}
.enrol{left:1025px;top:15px;width:63px;height:20px;background:var(--teal);color:#fff;font-size:7px;font-weight:600;text-align:center;line-height:20px}
.nav{left:730px;top:50px;display:flex;gap:30px;font-size:13px;color:#333}
.nav .active{color:var(--teal)}

/* hero */
.hero{left:0;top:78px;width:1200px;height:501px;background:linear-gradient(180deg,#7f93a8 0%,#b3c0cd 28%,#6f8461 45%,#4d6b2f 65%,#3f5a25 100%)}
.hero-title{left:0;top:255px;width:1200px;text-align:center;font-family:"Josefin Sans",sans-serif;font-weight:700;font-size:44px;color:#fff}
.hero-text{left:300px;top:324px;width:600px;text-align:center;font-size:13px;line-height:21px;color:#fff}
.hero-arrow{top:310px}

/* sidebar */
.sidebar{left:112px;top:495px;width:270px;height:548px;background:#fff;border-radius:16px;box-shadow:0 2px 12px rgba(0,0,0,.12);padding:19px 22px}
.pill{height:34px;border-radius:17px;background:var(--pill);font-family:"Josefin Sans",sans-serif;font-weight:600;font-size:14px;color:var(--dark);text-align:center;line-height:36px;margin-bottom:9px}
.pill.dark{background:var(--dark);color:#fff}
.side-intro{font-size:13px;line-height:21px;color:var(--muted);text-align:justify;margin:8px 0 12px}
.side-list{list-style:none;margin-bottom:12px}
.side-list li{font-size:13px;height:34.3px;line-height:20px;color:#555}
.side-list li::before{content:"»";margin-right:14px;color:#555}
.side-list li.active{color:var(--teal)}

/* article */
.article{left:433px;top:632px;width:655px}
.article h2{font-size:25px;margin-bottom:20px}
.article p{font-size:13px;line-height:25.7px;text-align:justify;margin-bottom:25px}
.checks{list-style:none;margin-bottom:22px}
.checks li{font-size:13px;height:34.3px;display:flex;align-items:center;gap:14px;color:#555}

/* journey banner */
.journey{left:0;top:1286px;width:1200px;height:379px;background:linear-gradient(180deg,#fafafa 0%,#f1f1f1 70%,#e6e8ea 100%)}
.journey-photo{left:900px;top:1286px;width:300px;height:379px;background:linear-gradient(135deg,#eef0f0,#d9dcdd 60%,#c7cacb)}
.journey-title{left:162px;top:1392px;font-size:38px;white-space:nowrap}
.journey-text{left:164px;top:1452px;width:590px;font-size:13px;line-height:25px;text-align:justify}
.btn{background:var(--teal);color:#fff;font-family:"Josefin Sans",sans-serif;font-weight:700;font-size:14px;text-align:center;border-radius:17px}
.journey-btn{left:164px;top:1520px;width:140px;height:32px;line-height:34px}

/* section headings */
.sec-title{font-size:38px;white-space:nowrap}
.view-all{width:139px;height:34px;line-height:36px}

/* jobs */
.job{width:312px;height:152px;background:#fff;box-shadow:0 2px 14px rgba(0,0,0,.08);border-radius:4px}
.job-avatar{left:26px;top:26px;width:34px;height:34px;border-radius:50%;background:#f2f2f2;font-family:"Roboto",sans-serif;font-weight:500;color:#333;font-size:15px;text-align:center;line-height:34px}
.job-title{left:77px;top:17px;width:225px;font-family:"Roboto",sans-serif;font-weight:500;font-size:16px;line-height:28px;color:#111}
.job-tags{left:26px;top:88px;display:flex;gap:8px}
.tag{font-size:8.5px;padding:3px 7px;background:#f2f2f2;color:#333}
.tag.teal{color:var(--teal)}
.job-posted{left:26px;top:115px;font-size:9px;color:#666;display:flex;align-items:center;gap:4px}

/* places */
.places{left:0;top:2278px;width:1200px;height:561px;background:var(--grey-bg)}
.place{top:2453px;width:234px;height:284px}
.place-label{left:0;bottom:28px;width:100%;text-align:center;font-family:"Josefin Sans",sans-serif;font-weight:700;font-size:20px;color:#fff}

/* posts */
.post-img{top:3007px;width:311px;height:196px}
.post-card{top:3185px;width:279px;height:135px;background:#fff;padding:8px 0 0 32px}
.post-cat{font-size:15px;color:#777;margin-bottom:10px}
.post-title{font-family:"Josefin Sans",sans-serif;font-weight:700;font-size:20px;line-height:22px;color:#222;margin-bottom:22px}
.post-meta{font-size:12px;color:#777;display:flex;justify-content:space-between;width:255px}

/* footer */
.footer{left:0;top:3420px;width:1200px;height:600px;background:var(--teal)}
.foot-brand{left:0;top:3470px;width:1200px;display:flex;justify-content:center;align-items:center;gap:10px}
.foot-brand .brand-mark{background:#fff;width:18px;height:18px}
.foot-brand span{font-weight:600;font-size:24px;color:#fff}
.foot-col{top:3562px;width:120px;text-align:center;color:#fff}
.foot-col h4{font-family:"Josefin Sans",sans-serif;font-size:11px;font-weight:700;margin-bottom:8px;line-height:12px}
.foot-col li{list-style:none;font-size:8.5px;line-height:11px;margin-bottom:12px}
.foot-strip{left:0;top:3838px;width:1200px;height:166px;background:linear-gradient(180deg,#5f8d94 0%,#3d6b57 45%,#2b4c3c 100%)}
.foot-info{left:0;width:1200px;text-align:center;color:#fff}
.pay{top:3939px;width:32px;height:18px;background:#fff;border-radius:3px}
.soc{top:3937px;width:22px;height:22px;border:1.5px solid #fff;border-radius:50%}
.copyright{left:0;top:4018px;width:1200px;text-align:center;font-size:11px;color:#555}
</style>
</head>
<body>

<header class="abs site-header">
  <div class="abs brand"><span class="brand-mark"></span><span class="brand-name">Bramblequill Institute</span></div>
  <div class="abs search"><span>SEARCH</span><span>GO</span></div>
  <div class="abs enrol">ENROL ME</div>
  <nav class="abs nav"><span>Home</span><span>Asia</span><span>Teach English Online</span><span class="active">South Korea</span></nav>
</header>

<section class="abs hero" role="img" aria-label="Mountain valley with terraced green fields under a cloudy sky"></section>
<h1 class="abs hero-title">Teach english in South Korea</h1>
<p class="abs hero-text">Lorem ipsum dolor sit amet, consectetur adipiscing elit, sed do eiusmod tempor incididunt ut labore et dolore magna aliqua. Ut enim ad minim veniam, quis nostrud exercitation ullamco laboris nisi ut aliquip ex ea commodo consequat.</p>
<svg class="abs hero-arrow" style="left:98px" width="14" height="26" viewBox="0 0 14 26"><path d="M12 2 2 13l10 11" fill="none" stroke="#fff" stroke-width="2.5"/></svg>
<svg class="abs hero-arrow" style="left:1088px" width="14" height="26" viewBox="0 0 14 26"><path d="M2 2l10 11L2 24" fill="none" stroke="#fff" stroke-width="2.5"/></svg>

<aside class="abs sidebar">
  <div class="pill dark">Introduction</div>
  <p class="side-intro">Lorem ipsum dolor sit amet, consectetur adipiscing elit, sed do eiusmod tempor incididunt ut labore et dolore magna aliqua.</p>
  <ul class="side-list">
    <li>Teaching Experience</li>
    <li class="active">Visa Requirements</li>
    <li>Certifications</li>
    <li>Degree Required</li>
    <li>Non Native English Speaker</li>
    <li>Healthcare &amp; Insurance</li>
  </ul>
  <div class="pill">Requirements</div>
  <div class="pill">Jobs &amp; Programmes</div>
  <div class="pill">Salaries and Benefits</div>
  <div class="pill">Cost of Living</div>
</aside>

<article class="abs article">
  <h2 class="head-font">Do you need a VISA to teach english abroad ?</h2>
  <p>Lorem ipsum dolor sit amet, consectetur adipiscing elit, sed do eiusmod tempor incididunt ut labore et dolore magna aliqua. Ut enim ad minim veniam, quis nostrud exercitation ullamco laboris nisi ut aliquip ex ea commodo consequat. Duis aute irure dolor in reprehenderit in voluptate velit esse cillum dolore eu fugiat nulla pariatur.</p>
  <p>Excepteur sint occaecat cupidatat non proident, sunt in culpa qui officia deserunt mollit anim id est laborum. Lorem ipsum dolor sit amet, consectetur adipiscing elit, sed do eiusmod tempor incididunt ut labore et dolore magna aliqua. Ut enim ad minim veniam, quis nostrud exercitation ullamco laboris nisi ut aliquip ex ea commodo consequat. Duis aute irure dolor in reprehenderit in voluptate velit esse cillum dolore eu fugiat nulla pariatur.</p>
  <ul class="checks">
    <li><svg width="13" height="13" viewBox="0 0 13 13"><circle cx="6.5" cy="6.5" r="6.5" fill="#1dc2c7"/><path d="M3.5 6.7 5.6 8.7 9.5 4.6" fill="none" stroke="#fff" stroke-width="1.6"/></svg>Nemo enim ipsam voluptatem quia voluptas</li>
    <li><svg width="13" height="13" viewBox="0 0 13 13"><circle cx="6.5" cy="6.5" r="6.5" fill="#1dc2c7"/><path d="M3.5 6.7 5.6 8.7 9.5 4.6" fill="none" stroke="#fff" stroke-width="1.6"/></svg>Lorem ipsum dolor sit amet, consectetur</li>
    <li><svg width="13" height="13" viewBox="0 0 13 13"><circle cx="6.5" cy="6.5" r="6.5" fill="#1dc2c7"/><path d="M3.5 6.7 5.6 8.7 9.5 4.6" fill="none" stroke="#fff" stroke-width="1.6"/></svg>Sed ut perspiciatis unde omnis</li>
    <li><svg width="13" height="13" viewBox="0 0 13 13"><circle cx="6.5" cy="6.5" r="6.5" fill="#1dc2c7"/><path d="M3.5 6.7 5.6 8.7 9.5 4.6" fill="none" stroke="#fff" stroke-width="1.6"/></svg>Nemo enim ipsam voluptatem quia voluptas</li>
  </ul>
  <p>Ut enim ad minim veniam, quis nostrud exercitation ullamco laboris nisi ut aliquip ex ea commodo consequat. Duis aute irure dolor in reprehenderit in voluptate velit esse cillum dolore eu fugiat nulla pariatur.</p>
</article>

<section class="abs journey"></section>
<div class="abs journey-photo" role="img" aria-label="Desk with a laptop corner, coffee cup, plant leaves, spiral notepad and pen"></div>
<h2 class="abs head-font journey-title">Your TEFL Journey Starts Here!</h2>
<p class="abs journey-text">Ut enim ad minim veniam, quis nostrud exercitation ullamco laboris nisi ut aliquip ex ea commodo consequat. Duis aute irure dolor in reprehenderit in voluptate velit esse cillum</p>
<div class="abs btn journey-btn">Starts Now</div>

<h2 class="abs head-font sec-title" style="left:109px;top:1762px">Teaching jobs in South korea</h2>
<div class="abs btn view-all" style="left:949px;top:1770px">View All</div>

<div class="abs job" style="left:109px;top:1843px"><div class="abs job-avatar">L</div><div class="abs job-title">Lorem ipsum dolor sit amet, consectetur adipiscing</div><div class="abs job-tags"><span class="tag teal">SOUTH KOREA</span><span class="tag">ROAMGRADE</span></div><div class="abs job-posted">◷ Posted 4 days ago</div></div>
<div class="abs job" style="left:443px;top:1843px"><div class="abs job-avatar">L</div><div class="abs job-title">Lorem ipsum dolor sit amet, consectetur adipiscing</div><div class="abs job-tags"><span class="tag teal">SOUTH KOREA</span><span class="tag">ROAMGRADE</span></div><div class="abs job-posted">◷ Posted 4 days ago</div></div>
<div class="abs job" style="left:777px;top:1843px"><div class="abs job-avatar">L</div><div class="abs job-title">Lorem ipsum dolor sit amet, consectetur adipiscing</div><div class="abs job-tags"><span class="tag teal">SOUTH KOREA</span><span class="tag">ROAMGRADE</span></div><div class="abs job-posted">◷ Posted 4 days ago</div></div>
<div class="abs job" style="left:109px;top:2023px"><div class="abs job-avatar">L</div><div class="abs job-title">Lorem ipsum dolor sit amet, consectetur adipiscing</div><div class="abs job-tags"><span class="tag teal">SOUTH KOREA</span><span class="tag">ROAMGRADE</span></div><div class="abs job-posted">◷ Posted 4 days ago</div></div>
<div class="abs job" style="left:443px;top:2023px"><div class="abs job-avatar">L</div><div class="abs job-title">Lorem ipsum dolor sit amet, consectetur adipiscing</div><div class="abs job-tags"><span class="tag teal">SOUTH KOREA</span><span class="tag">ROAMGRADE</span></div><div class="abs job-posted">◷ Posted 4 days ago</div></div>
<div class="abs job" style="left:777px;top:2023px"><div class="abs job-avatar">L</div><div class="abs job-title">Lorem ipsum dolor sit amet, consectetur adipiscing</div><div class="abs job-tags"><span class="tag teal">SOUTH KOREA</span><span class="tag">ROAMGRADE</span></div><div class="abs job-posted">◷ Posted 4 days ago</div></div>

<section class="abs places"></section>
<h2 class="abs head-font sec-title" style="left:109px;top:2376px">Other popular places to teach in Asia</h2>
<div class="abs btn view-all" style="left:949px;top:2384px">View All</div>
<div class="abs place" style="left:111px;background:linear-gradient(180deg,#c98aa4,#8c6a78 50%,#4e4550)" role="img" aria-label="Ornate cathedral towers under a pink sky"><div class="abs place-label">Duis aute irure</div></div>
<div class="abs place" style="left:359px;background:linear-gradient(180deg,#e9d6b8,#c9a77c 55%,#7a8d86)" role="img" aria-label="Whitewashed courtyard with a small pool"><div class="abs place-label">Duis aute irure</div></div>
<div class="abs place" style="left:607px;background:linear-gradient(180deg,#8fa7c4,#5b5d63 45%,#2e2f35)" role="img" aria-label="Carved temple facade with gold details"><div class="abs place-label">Duis aute irure</div></div>
<div class="abs place" style="left:855px;background:linear-gradient(180deg,#d9a9b4,#b8b9c8 45%,#55697a)" role="img" aria-label="White island houses and a windmill at dusk"><div class="abs place-label">Duis aute irure</div></div>

<h2 class="abs head-font sec-title" style="left:109px;top:2937px">Related Posts</h2>
<div class="abs btn view-all" style="left:949px;top:2945px">View All</div>
<div class="abs post-img" style="left:111px;background:linear-gradient(180deg,#6f8f4a,#4c6a33 55%,#8a7a5a)" role="img" aria-label="Traveller seated among tropical plants"></div>
<div class="abs post-img" style="left:445px;background:linear-gradient(180deg,#d7c9b5,#8e9b8c 50%,#3f5a3d)" role="img" aria-label="Traveller on a rock overlooking a bay at sunset"></div>
<div class="abs post-img" style="left:778px;background:linear-gradient(180deg,#b9c6cf,#7c8284 55%,#4a4c48)" role="img" aria-label="Traveller wading among rocks on a shoreline"></div>
<div class="abs post-card" style="left:111px"><div class="post-cat">Duis aute irure dolor</div><div class="post-title">Lorem ipsum dolor sit amet, consectetur</div><div class="post-meta"><span>👤 Nora Wells Avery</span><span>▦ Mar 13, 2023</span></div></div>
<div class="abs post-card" style="left:445px"><div class="post-cat">Duis aute irure dolor</div><div class="post-title">Lorem ipsum dolor sit amet, consectetur</div><div class="post-meta"><span>👤 Nora Wells Avery</span><span>▦ Mar 13, 2023</span></div></div>
<div class="abs post-card" style="left:778px"><div class="post-cat">Duis aute irure dolor</div><div class="post-title">Lorem ipsum dolor sit amet, consectetur</div><div class="post-meta"><span>👤 Nora Wells Avery</span><span>▦ Mar 13, 2023</span></div></div>

<footer>
  <div class="abs footer"></div>
  <div class="abs foot-brand"><span class="brand-mark"></span><span>Bramblequill Institute</span></div>
  <div class="abs foot-col" style="left:270px"><h4>Why BQI?</h4><ul><li>Why Choose Us?</li><li>Charity Partnership</li><li>Accreditation</li><li>Compare TEFL Course Providers</li><li>Meet our Alumni</li><li>Meet our Trainers</li><li>Company profile</li><li>Testimonials</li><li>Affiliate Programme</li></ul></div>
  <div class="abs foot-col" style="left:406px"><h4>TEFL Courses</h4><ul><li>View All TEFL Courses</li><li>Online TEFL Course (Level 3 – 120hrs)</li><li>Online TEFL Course (Level 5 – 168hrs)</li><li>Observed Teaching Practice Course (Level 5)</li><li>TEFL Top-Up Courses</li></ul></div>
  <div class="abs foot-col" style="left:540px"><h4>Teaching Opportunities</h4><ul><li>TEFL Jobs</li><li>TEFL Internships</li><li>TEFL Volunteering</li><li>Country Profiles</li><li>Teaching without a Degree</li></ul></div>
  <div class="abs foot-col" style="left:675px"><h4>Student Support Centre</h4><ul><li>TEFL Learning Centre</li><li>Frequently Asked Questions</li></ul></div>
  <div class="abs foot-col" style="left:810px"><h4>Talk to Us</h4><ul><li>Get in Touch</li><li>Request Call Back</li><li>Blog</li></ul></div>
  <div class="abs foot-strip" role="img" aria-label="Tropical palms and a thatched roof in deep green tones"></div>
  <div class="abs foot-info" style="top:3898px;font-size:9px;font-weight:600">Call us for help +1 555 210 7733</div>
  <div class="abs foot-info" style="top:3941px;font-size:8px">Bramblequill Institute, 18 Harbor Row, Suite 4, Easton, ME 04740, USA</div>
  <div class="abs foot-info" style="top:3967px;font-size:7.5px">Terms and Conditions &nbsp;|&nbsp; Privacy Policy</div>
  <div class="abs pay" style="left:18px"></div><div class="abs pay" style="left:72px"></div><div class="abs pay" style="left:126px"></div><div class="abs pay" style="left:180px"></div><div class="abs pay" style="left:234px"></div><div class="abs pay" style="left:284px"></div>
  <div class="abs soc" style="left:1033px"></div><div class="abs soc" style="left:1064px"></div><div class="abs soc" style="left:1096px"></div><div class="abs soc" style="left:1128px"></div><div class="abs soc" style="left:1160px"></div>
  <div class="abs copyright">© Copyrights 2023 Company Name | All Rights reserved</div>
</footer>

</body>
</html>
```